Portal Panel Medic need professional looking business card printed on plastic, Commericial, Industri

We are family owned and operated garage door company in Indianapolis, Indiana. We sale service and install dock equipment, doors, operators. We are looking to expand our commercial/ industrial division. We also service all residential doors and operators. We are looking for a business that stands out of the crowd. We are committed to have the best customer service in the industry.

Target Market(s)

National and local general contractors, National/ Corpate service accounts,

Industry/Entity Type

Business Service

Contact Information for Business Card

To be printed on plastic stock

Font styles to use
Sans Serif

Colors
ffffff
f04a50
ec1f27

Requirements
Must have
• Name, website,email, phone number, position.
Nice to have
• A standout professional design

```html
<!DOCTYPE html>
<html lang="en">
<head>
<meta charset="utf-8">
<title>Portal Panel Medic – Business Card</title>
<link rel="stylesheet" href="https://fonts.googleapis.com/css2?family=Open+Sans:wght@600;700;800&family=Arimo:wght@400&display=swap">
<style>
  :root {
    --canvas: #d6d6d6;
    --card: #ffffff;
    --red: #ec1f27;
    --red-soft: #f04a50;
    --ink: #111111;
  }
  * { margin: 0; padding: 0; box-sizing: border-box; }
  html, body { width: 1189px; height: 1200px; overflow: hidden; background: var(--canvas); }
  body { position: relative; font-family: "Arimo", Arial, sans-serif; color: var(--ink); }

  .card {
    position: absolute; left: 166px; width: 857px; height: 488px;
    background: var(--card); border-radius: 30px;
  }
  .card--front { top: 67px; }
  .card--back  { top: 626px; }

  .brand-name {
    position: absolute; font-family: "Open Sans", sans-serif; font-weight: 800;
    color: var(--red); text-transform: uppercase; text-align: center; line-height: 0.98;
  }
  .tagline {
    position: absolute; font-family: "Open Sans", sans-serif; font-weight: 600;
    color: var(--red); text-align: center; white-space: nowrap;
  }
  .hotline {
    position: absolute; font-family: "Open Sans", sans-serif; font-weight: 700;
    color: var(--red); text-align: center; white-space: nowrap; line-height: 1;
  }
  .hotline .area { font-size: 0.72em; margin-right: 6px; }

  /* front */
  .card--front .brand-name { left: 0; width: 100%; top: 140px; font-size: 50px; }
  .card--front .tagline { left: 0; width: 100%; top: 302px; font-size: 12px; }
  .card--front .hotline { left: 0; width: 100%; top: 320px; font-size: 38px; }
  .web-spaced {
    position: absolute; left: 0; width: 100%; top: 394px; text-align: center;
    font-size: 19px; letter-spacing: 6.5px;
  }

  /* back */
  .card--back .brand-name { left: 86px; width: 260px; top: 150px; font-size: 40px; }
  .card--back .tagline { left: 91px; width: 250px; top: 298px; font-size: 10px; }
  .card--back .hotline { left: 91px; width: 250px; top: 317px; font-size: 33px; }
  .divider { position: absolute; left: 412px; top: 153px; width: 1px; height: 192px; background: var(--red-soft); }

  .contact-block { position: absolute; left: 469px; top: 150px; }
  .person-name { font-size: 26px; line-height: 1; }
  .person-role { color: var(--red); font-size: 19px; line-height: 1; margin-top: 1px; }
  .address { font-size: 19px; line-height: 25px; margin-top: 17px; }
  .contact-list { list-style: none; margin-top: 9px; }
  .contact-list li { display: flex; align-items: center; gap: 11px; font-size: 19px; height: 26px; }
  .contact-list svg { width: 20px; height: 20px; flex: none; }
</style>
</head>
<body>

<section class="card card--front">
  <div class="brand-name">Portal<br>Panel Medic</div>
  <p class="tagline">"Expert Service at an Affordable Price"</p>
  <p class="hotline"><span class="area">(555)</span>214-0198</p>
  <p class="web-spaced">www.portalpanelmedic.com</p>
</section>

<section class="card card--back">
  <div class="brand-name">Portal<br>Panel<br>Medic</div>
  <p class="tagline">"Expert Service at an Affordable Price"</p>
  <p class="hotline"><span class="area">(555)</span>214-0198</p>
  <span class="divider"></span>

  <div class="contact-block">
    <p class="person-name">Jordan Blake</p>
    <p class="person-role">Director</p>
    <p class="address">PO BOX 123 your address<br>2nd street Melbourne</p>
    <ul class="contact-list">
      <li>
        <svg viewBox="0 0 20 20" aria-hidden="true"><rect width="20" height="20" fill="#ec1f27"/><path d="M6 4l2.5 0 1 3-1.5 1.2c.8 1.6 2 2.8 3.6 3.6L12.8 10.3l3 1 0 2.6c0 .6-.5 1.1-1.1 1.1C9.2 15 5 10.8 5 5.1 5 4.5 5.4 4 6 4z" fill="#fff"/></svg>
        (123) 456-7890
      </li>
      <li>
        <svg viewBox="0 0 20 20" aria-hidden="true"><rect width="20" height="20" fill="#ec1f27"/><rect x="4" y="6" width="12" height="8.5" fill="none" stroke="#fff" stroke-width="1.4"/><path d="M4 6l6 5 6-5" fill="none" stroke="#fff" stroke-width="1.4"/></svg>
        info@portalpanelmedic.com
      </li>
      <li>
        <svg viewBox="0 0 20 20" aria-hidden="true"><rect width="20" height="20" fill="#ec1f27"/><g fill="none" stroke="#fff" stroke-width="1.2"><circle cx="10" cy="10" r="6"/><ellipse cx="10" cy="10" rx="2.6" ry="6"/><path d="M4 10h12M5 7h10M5 13h10"/></g></svg>
        www.portalpanelmedic.com
      </li>
    </ul>
  </div>
</section>

</body>
</html>
```